Now Leasing Banner

Looking for a banner that says the following information approx 4' x 30'

Now Leasing Maple Ridge Court 925-318-6042

Target Market(s)

Drive by traffic

Industry/Entity Type

Residential property management

Requirements
Must have
• Clear and readable from a distance

```html
<!DOCTYPE html>
<html lang="en">
<head>
<meta charset="utf-8">
<title>Now Leasing Banner – Maple Ridge Court</title>
<link href="https://fonts.googleapis.com/css2?family=Khand:wght@600;700&family=Roboto:wght@700&display=swap" rel="stylesheet">
<style>
  :root {
    --navy: #1b3f8f;
    --navy-dark: #0f2a66;
    --sky: #0aa3d6;
    --ink: #161616;
    --grey-text: #474747;
    --dim-blue: #2a6db5;
    --dim-line: #9fb3dd;
    --paper: #ffffff;
    --page: #fdfdfd;
  }
  * { margin: 0; padding: 0; box-sizing: border-box; }
  html, body { width: 1200px; height: 675px; overflow: hidden; background: var(--page); }
  .canvas { position: relative; width: 1200px; height: 675px; }
  .shapes { position: absolute; inset: 0; }
  .dim-label {
    position: absolute;
    font-family: "Roboto", Arial, sans-serif;
    font-weight: 700;
    font-size: 15px;
    color: var(--dim-blue);
    background: var(--page);
    line-height: 1;
  }
  .dim-width { left: 597px; top: 250px; padding: 0 4px; }
  .dim-height { left: 28px; top: 341px; transform: rotate(-90deg); padding: 0 2px; }
  .headline {
    position: absolute;
    font-family: "Khand", "Arial Narrow", sans-serif;
    line-height: 1;
    white-space: nowrap;
  }
  .now-leasing {
    left: 334px; top: 289px;
    font-size: 60px; font-weight: 600;
    color: var(--grey-text);
    letter-spacing: -1px;
  }
  .property-name {
    left: 381px; top: 352px;
    font-size: 61px; font-weight: 700;
    color: var(--navy);
    letter-spacing: -0.5px;
  }
  .phone-number {
    left: 866px; top: 320px;
    font-size: 58px; font-weight: 700;
    color: var(--paper);
    text-shadow: 3px 3px 0 rgba(0,0,0,0.55);
    letter-spacing: -0.5px;
  }
</style>
</head>
<body>
<div class="canvas">
  <svg class="shapes" width="1200" height="675" viewBox="0 0 1200 675" xmlns="http://www.w3.org/2000/svg">
    <defs>
      <linearGradient id="photoTone" x1="0" y1="0" x2="1" y2="1">
        <stop offset="0" stop-color="#8c99a6"/>
        <stop offset="0.5" stop-color="#c9ced3"/>
        <stop offset="1" stop-color="#3e4756"/>
      </linearGradient>
      <linearGradient id="peakTone" x1="0" y1="0" x2="0" y2="1">
        <stop offset="0" stop-color="#c4c4c4"/>
        <stop offset="1" stop-color="#ededed"/>
      </linearGradient>
    </defs>

    <!-- dimension lines -->
    <g class="dimensions" stroke="var(--dim-line)" stroke-width="1" fill="none">
      <path d="M52.5 274 V257.5 H1171 V274"/>
      <path d="M52 274 H35.5 V424 H52"/>
    </g>

    <!-- banner base -->
    <rect class="banner" x="52.5" y="274" width="1118.5" height="150" fill="var(--paper)"/>

    <!-- photo area -->
    <path class="photo" role="img" aria-label="Photo of two people shaking hands over a signed lease contract"
          d="M52.5 274 H297 Q272 380 212 424 H52.5 Z" fill="url(#photoTone)"/>
    <path class="swoosh" d="M297 274 H325 Q292 385 205 424 H196 Q268 378 297 274 Z" fill="var(--navy)"/>

    <!-- mountain decoration -->
    <rect class="peaks" role="img" aria-label="Grey mountain range decoration"
          x="612" y="291" width="166" height="53" fill="url(#peakTone)"/>

    <!-- location pin -->
    <g class="pin-icon">
      <path d="M353 360 C343 360 336 367 336 377 C336 389 353 411 353 411 C353 411 370 389 370 377 C370 367 363 360 353 360 Z" fill="var(--sky)"/>
      <circle cx="353" cy="377" r="6" fill="var(--paper)"/>
    </g>

    <!-- contact panel -->
    <rect class="contact-panel" x="811" y="274" width="360" height="150" fill="var(--navy)"/>
    <polygon class="ribbon-fold" points="797,386 811,386 811,400" fill="var(--navy-dark)"/>
    <rect class="ribbon" x="797" y="312" width="374" height="74" fill="var(--sky)"/>
    <polygon class="ribbon-strip" points="859,312 1147,312 1171,386 876,386" fill="var(--ink)"/>

    <!-- phone icon -->
    <g class="phone-icon">
      <circle cx="832.5" cy="346" r="20" fill="var(--paper)"/>
      <path d="M825 335 L829 333 L832 340 L829 342 C830 346 832 349 836 351 L838 348 L845 351 L843 355 C841 357 838 357 835 355 C829 352 825 347 823 341 C822 338 823 336 825 335 Z" fill="var(--navy)"/>
    </g>

    <!-- banner outline -->
    <rect x="52.5" y="274" width="1118.5" height="150" fill="none" stroke="#333" stroke-width="0.8"/>
  </svg>

  <span class="dim-label dim-width">30'</span>
  <span class="dim-label dim-height">4'</span>

  <div class="headline now-leasing">Now Leasing</div>
  <div class="headline property-name">Maple Ridge Court</div>
  <div class="headline phone-number">925-318-6042</div>
</div>
</body>
</html>
```